Bill board design For Marlowe’s Construction

Billboard Design Request
Please design the billboard to match the branding, colors, and overall feel of our website: Marlowe's Construction Website
MARLOWE’S CONSTRUCTION
CONCRETE BUILT FOR GENERATIONS
⭐ 5-Star Rated on Zorvix
Please Include:
* All three attached project photos
* Company logo(s)
* Phone Number: 555-214-7630
* Website: MarlowesConstruction.example
* Zorvix logo with 5-star rating graphic
* Chatterly logo
* Pixtoria logo
Service Area:
Ashbrook • Willow Ferry • Stonehaven • Harlow Ridge
Please arrange the photos and layout in whatever way creates the strongest visual impact and readability from the road. The company name, headline, phone number, and website should be highly visible at highway speeds.
The overall appearance should be clean, professional, premium, and consistent with our website branding while highlighting our reputation, craftsmanship, and quality concrete work.
People Driving By
Concrete Construction

```html
<!DOCTYPE html>
<html lang="en">
<head>
<meta charset="utf-8">
<title>Marlowe’s Construction Billboard</title>
<link href="https://fonts.googleapis.com/css2?family=Montserrat:wght@500;600;700;800&display=swap" rel="stylesheet">
<style>
  :root {
    --brand-blue: #2f8fd6;
    --brand-grey: #6b6b6b;
    --ink: #1d1d1d;
    --band-grey: #676767;
    --bar-black: #050505;
    --paper: #ffffff;
    --backdrop: #e8ecf1;
    --star: #f4b400;
  }
  * { box-sizing: border-box; margin: 0; padding: 0; }
  html, body { width: 1200px; height: 828px; overflow: hidden; }
  body {
    background: var(--backdrop);
    font-family: "Montserrat", Arial, sans-serif;
    position: relative;
  }
  .billboard {
    position: absolute;
    left: 20px; top: 171px;
    width: 1160px; height: 486px;
    background: var(--paper);
    overflow: hidden;
    box-shadow: 0 6px 24px rgba(0,0,0,.18);
  }
  .brand {
    position: absolute;
    left: 30px; top: 30px;
    width: 330px; height: 185px;
    display: flex; flex-direction: column; align-items: center; justify-content: flex-end;
    text-align: center;
  }
  .brand-square {
    width: 100px; height: 100px;
    background: var(--brand-blue);
    margin-bottom: 16px;
  }
  .brand-name { font-size: 42px; font-weight: 800; line-height: 1; letter-spacing: -0.5px; color: var(--brand-blue); }
  .brand-sub { font-size: 15px; font-weight: 600; letter-spacing: 5.5px; margin-top: 6px; color: var(--brand-grey); }
  .divider {
    position: absolute;
    left: 379px; top: 40px;
    width: 3px; height: 176px;
    background: var(--brand-grey);
  }
  .headline {
    position: absolute;
    left: 404px; top: 44px;
    color: var(--brand-blue);
    font-weight: 800;
    font-size: 74px;
    line-height: 1.1;
    letter-spacing: -1px;
    white-space: nowrap;
  }
  .service-band {
    position: absolute;
    left: 38px; top: 228px;
    width: 1084px; height: 48px;
    background: var(--band-grey);
    clip-path: polygon(0 0, 100% 0, 98.8% 50%, 100% 100%, 0 100%, 1.2% 50%);
    display: flex; align-items: center; justify-content: center;
    gap: 10px;
    color: var(--paper);
    font-size: 22px; font-weight: 600;
    white-space: nowrap;
  }
  .service-band strong { font-weight: 800; }
  .project-photo {
    position: absolute;
    top: 283px; height: 120px;
  }
  .photo-crew { left: 38px; width: 199px; background: linear-gradient(160deg, #7a8a5a, #4a4038 60%, #9a8a78); }
  .photo-garage { left: 245px; width: 199px; background: linear-gradient(180deg, #8fa86a 0%, #9a6a4e 40%, #d8d6d0 70%, #c9c6bf); }
  .photo-walkway { left: 451px; width: 194px; background: linear-gradient(180deg, #6c5a4a 0%, #5d6e44 40%, #b86a42 70%, #a35a38); }
  .rating {
    position: absolute;
    left: 670px; top: 294px;
    width: 250px;
    text-align: center;
  }
  .rating-name {
    font-size: 62px; font-weight: 700;
    color: var(--brand-blue);
    line-height: 1;
    letter-spacing: -1px;
  }
  .rating-stars { display: flex; justify-content: center; gap: 3px; margin-top: 2px; }
  .rating-stars svg { width: 22px; height: 22px; fill: var(--star); }
  .rating-text {
    position: absolute;
    left: 936px; top: 318px;
    color: var(--ink);
    font-size: 23px; font-weight: 700;
    line-height: 1.3;
  }
  .contact-bar {
    position: absolute;
    left: 0; bottom: 0;
    width: 100%; height: 76px;
    background: var(--bar-black);
    display: flex; align-items: center; justify-content: space-between;
    padding: 0 34px;
    white-space: nowrap;
  }
  .contact-item { display: flex; align-items: center; gap: 10px; }
  .contact-item svg { flex: none; }
  .phone { color: var(--brand-blue); font-size: 40px; font-weight: 800; letter-spacing: -0.5px; }
  .website { color: var(--brand-blue); font-size: 23px; font-weight: 700; }
  .bar-rule { width: 3px; height: 40px; background: var(--paper); }
  .follow { color: var(--paper); font-size: 16px; font-weight: 700; gap: 8px; }
</style>
</head>
<body>
  <main class="billboard">
    <div class="brand">
      <div class="brand-square"></div>
      <div class="brand-name">MARLOWE’S</div>
      <div class="brand-sub">CONSTRUCTION L.L.C</div>
    </div>

    <div class="divider"></div>

    <h1 class="headline">CONCRETE BUILT<br>FOR GENERATIONS</h1>

    <div class="service-band">
      <strong>SERVICE AREA</strong> • ASHBROOK • WILLOW FERRY • STONEHAVEN • HARLOW RIDGE
    </div>

    <div class="project-photo photo-crew" role="img" aria-label="Crew member finishing fresh concrete with a float tool"></div>
    <div class="project-photo photo-garage" role="img" aria-label="New concrete driveway leading to a brick garage"></div>
    <div class="project-photo photo-walkway" role="img" aria-label="Stamped reddish concrete walkway leading to a house"></div>

    <div class="rating">
      <div class="rating-name">Zorvix</div>
      <div class="rating-stars" aria-label="5 stars">
        <svg viewBox="0 0 24 24"><path d="M12 2l2.9 6.6 7.1.6-5.4 4.7 1.6 7-6.2-3.7-6.2 3.7 1.6-7L2 9.2l7.1-.6z"/></svg>
        <svg viewBox="0 0 24 24"><path d="M12 2l2.9 6.6 7.1.6-5.4 4.7 1.6 7-6.2-3.7-6.2 3.7 1.6-7L2 9.2l7.1-.6z"/></svg>
        <svg viewBox="0 0 24 24"><path d="M12 2l2.9 6.6 7.1.6-5.4 4.7 1.6 7-6.2-3.7-6.2 3.7 1.6-7L2 9.2l7.1-.6z"/></svg>
        <svg viewBox="0 0 24 24"><path d="M12 2l2.9 6.6 7.1.6-5.4 4.7 1.6 7-6.2-3.7-6.2 3.7 1.6-7L2 9.2l7.1-.6z"/></svg>
        <svg viewBox="0 0 24 24"><path d="M12 2l2.9 6.6 7.1.6-5.4 4.7 1.6 7-6.2-3.7-6.2 3.7 1.6-7L2 9.2l7.1-.6z"/></svg>
      </div>
    </div>
    <p class="rating-text">5-STAR RATED<br>ON ZORVIX</p>

    <footer class="contact-bar">
      <div class="contact-item">
        <svg width="30" height="30" viewBox="0 0 24 24" fill="#ffffff" aria-hidden="true"><path d="M6.6 10.8a15.1 15.1 0 006.6 6.6l2.2-2.2a1 1 0 011-.25 11.4 11.4 0 003.6.57 1 1 0 011 1V20a1 1 0 01-1 1A17 17 0 013 4a1 1 0 011-1h3.5a1 1 0 011 1 11.4 11.4 0 00.57 3.6 1 1 0 01-.25 1z"/></svg>
        <span class="phone">555-214-7630</span>
      </div>
      <div class="bar-rule"></div>
      <div class="contact-item">
        <svg width="26" height="26" viewBox="0 0 24 24" fill="none" stroke="#ffffff" stroke-width="1.6" aria-hidden="true"><circle cx="12" cy="12" r="10"/><ellipse cx="12" cy="12" rx="4.5" ry="10"/><path d="M2 12h20M4 6.5h16M4 17.5h16"/></svg>
        <span class="website">MarlowesConstruction.example</span>
      </div>
      <div class="bar-rule"></div>
      <div class="contact-item follow">FOLLOW US <span>Chatterly</span> <span>Pixtoria</span></div>
    </footer>
  </main>
</body>
</html>
```